VARNOLA SYSTEMS BUSINESS CARD DESIGN

WE WANT COMPLETE NEW DESIGN OF OUR BUSINESS CARD. WE ARE AN INTEGRATION COMPANY, WHERE WE INTEGRATE IOT/SMART SYSTEMS TO HOMES AND CORPORATE CUSTOMERS. WE SUPPLY AND INSTALL AUTOMATION PRODUCTS. THE FINAL DESIGN SHOULD COMMUNICATE TECHNOLOGY. THE CARD DESIGN SHOULD BE VERY IMPACT FULL. LOGO NEEDS TO BE THERE. IT WOULD NICE IF THE DESIGN WAS CLEAN. COLORS IS UP TO DESIGNER TO PLAY WITH, OR CAN STICK TO CORPORATE COLORS (FOLLOW LOGO). I HAVE ADDED FEW REFERENCE PHOTOS TO DRAW INSPIRATION MAYBE. I HAVE ADDED A HEX DESIGN, ITS NOT NECESSARY TO USE THIS DESIGN, ITS UPTO DESIGNER, JUST ADDED IF NEEDED TO PLAY WITH DESIGN.

Target Market(s)

Private end users and corporate clients

Industry/Entity Type

technology, home automation, home theaters, building management systems, IOT

Contact Information for Business Card

It should include GERALD MOSSANE, personal number, office number, email address, both in English and arabic. DETAILS TO INCLUDE :GERALD MOSSANE, MOBILE 0097150738915,OFFCIE 009714386207, GERALD@VARNOLAHUB.CO

Requirements
Must have
• Should feel like a technology company from design. Details both and in English and arabic (or at least have provision for arabic in design).
Nice to have
• I would like logo on one side, and details on the other side. Logo design side should communicate technology with logo. Other side can be clean just with information or also have some design aspects following from logo side. it would be interesting to see submissions with square design as well (that looks like an app Icon). colors could be of logo, red black grey and white. I have added some designs to draw inspiration from

```html
<!DOCTYPE html>
<html lang="en">
<head>
<meta charset="utf-8">
<title>Varnola Systems — Business Card</title>
<link rel="stylesheet" href="https://fonts.googleapis.com/css2?family=Michroma&family=Jura:wght@300;400&family=Noto+Kufi+Arabic:wght@400&display=swap">
<style>
  :root{
    --bg:#d9d9d9;
    --paper:#f4f4f4;
    --ink:#111214;
    --dark:#15171a;
    --dark-2:#0b0c0e;
    --magenta:#d3124f;
    --blue:#1f4fb8;
    --cyan:#3ab7e0;
    --green:#22b04a;
    --lime:#8fd12a;
    --yellow:#f0d81a;
    --orange:#f08a12;
    --icon-orange:#e5831c;
    --icon-red:#d62828;
    --icon-green:#3aa12f;
    --icon-blue:#1c7fe0;
  }
  *{box-sizing:border-box;margin:0;padding:0}
  html,body{width:1200px;height:800px;overflow:hidden;background:var(--bg)}
  .canvas{position:relative;width:1200px;height:800px;display:flex;align-items:center;justify-content:center;gap:60px}
  .card{position:relative;width:520px;height:297px;overflow:hidden;box-shadow:0 10px 24px rgba(0,0,0,.18)}

  /* Logo side */
  .card--front{background:var(--paper)}
  .spectrum-strip{position:absolute;top:0;left:0;right:0;height:14px;
    background:linear-gradient(90deg,var(--magenta),var(--blue) 22%,var(--cyan) 40%,var(--green) 58%,var(--lime) 72%,var(--yellow) 88%,var(--orange))}
  .brand{position:absolute;left:0;right:0;top:50%;transform:translateY(-40%);display:flex;flex-direction:column;align-items:center;gap:10px}
  .brand__row{display:flex;align-items:center;gap:10px}
  .brand__mark{width:22px;height:22px;background:var(--icon-red)}
  .brand__name{font-family:"Michroma",sans-serif;font-size:22px;color:var(--ink);letter-spacing:1px}
  .brand__tagline{font-family:"Michroma",sans-serif;font-size:8px;color:var(--ink);letter-spacing:3px}

  /* Details side */
  .card--back{background:linear-gradient(180deg,var(--dark),var(--dark-2))}
  .spectrum-field{position:absolute;top:0;left:0;right:0;height:138px;
    background:linear-gradient(90deg,var(--magenta),#8a1d8f 14%,var(--blue) 26%,var(--cyan) 42%,#7fd9c8 50%,var(--green) 62%,var(--lime) 74%,var(--yellow) 86%,var(--orange))}
  .identity{position:absolute;left:0;right:0;top:44px;text-align:center}
  .identity__name{font-family:"Michroma",sans-serif;font-weight:400;font-size:24px;color:var(--ink);letter-spacing:.5px}
  .identity__role{font-family:"Jura",sans-serif;font-weight:300;font-size:16px;color:#1d2a3a;letter-spacing:1px;margin-top:2px;padding-left:70px}
  .identity__name-ar{font-family:"Noto Kufi Arabic",sans-serif;font-size:11px;color:var(--ink);margin-top:2px;padding-left:70px}

  .contact{position:absolute;display:flex;align-items:center;gap:12px;font-family:"Jura",sans-serif;font-size:10px;line-height:1.4}
  .contact__icon{width:30px;height:30px;display:flex;align-items:center;justify-content:center;flex:none}
  .contact__icon svg{width:16px;height:16px;fill:#111}
  .contact--phone{left:80px;top:164px;color:var(--icon-orange)}
  .contact--phone .contact__icon{background:var(--icon-orange)}
  .contact--mail{left:80px;top:218px;color:var(--icon-red)}
  .contact--mail .contact__icon{background:var(--icon-red)}
  .contact--web{left:290px;top:150px;color:var(--icon-green)}
  .contact--web .contact__icon{background:var(--icon-green)}
  .contact--address{left:290px;top:200px;color:var(--icon-blue)}
  .contact--address .contact__icon{background:var(--icon-blue)}
  .contact--address .contact__text span{display:inline-block;margin-right:14px}
  .contact__label{opacity:.75;margin-right:4px}

  .edge-bar{position:absolute;left:0;right:0;bottom:0;height:4px;display:flex}
  .edge-bar span{flex:1}
  .edge-bar span:nth-child(1){background:var(--icon-red)}
  .edge-bar span:nth-child(2){background:var(--icon-orange)}
  .edge-bar span:nth-child(3){background:var(--icon-blue)}
  .edge-bar span:nth-child(4){background:var(--icon-green)}
</style>
</head>
<body>
<main class="canvas">

  <section class="card card--front" aria-label="Business card, logo side">
    <div class="spectrum-strip"></div>
    <div class="brand">
      <div class="brand__row">
        <span class="brand__mark"></span>
        <span class="brand__name">VARNOLA SYSTEMS</span>
      </div>
      <span class="brand__tagline">A VARNOLA GROUP DIVISION</span>
    </div>
  </section>

  <section class="card card--back" aria-label="Business card, details side">
    <div class="spectrum-field" role="img" aria-label="Low-poly faceted rainbow pattern from magenta through blue, green and yellow to orange"></div>
    <div class="identity">
      <h1 class="identity__name">GERALD MOSSANE</h1>
      <p class="identity__role">DESIGNATION</p>
      <p class="identity__name-ar" lang="ar" dir="rtl">جيرالد موسان</p>
    </div>

    <div class="contact contact--phone">
      <span class="contact__icon"><svg viewBox="0 0 24 24"><path d="M6.6 10.8a15.1 15.1 0 0 0 6.6 6.6l2.2-2.2a1 1 0 0 1 1-.25 11.4 11.4 0 0 0 3.6.57 1 1 0 0 1 1 1V20a1 1 0 0 1-1 1A17 17 0 0 1 3 4a1 1 0 0 1 1-1h3.5a1 1 0 0 1 1 1c0 1.25.2 2.45.57 3.57a1 1 0 0 1-.25 1z"/></svg></span>
      <span class="contact__text">
        <span class="contact__label">M</span>0097150738915<br>
        <span class="contact__label">O</span>009714386207
      </span>
    </div>

    <div class="contact contact--mail">
      <span class="contact__icon"><svg viewBox="0 0 24 24"><path d="M3 5h18v14H3z" fill="none" stroke="#111" stroke-width="2"/><path d="M3 6l9 7 9-7" fill="none" stroke="#111" stroke-width="2"/></svg></span>
      <span class="contact__text">gerald@varnolahub.co</span>
    </div>

    <div class="contact contact--web">
      <span class="contact__icon"><svg viewBox="0 0 24 24"><circle cx="12" cy="12" r="9" fill="none" stroke="#111" stroke-width="2"/><path d="M3 12h18M12 3c3 3 3 15 0 18M12 3c-3 3-3 15 0 18" fill="none" stroke="#111" stroke-width="1.6"/></svg></span>
      <span class="contact__text">www.varnolasystems.co</span>
    </div>

    <div class="contact contact--address">
      <span class="contact__icon"><svg viewBox="0 0 24 24"><path d="M12 3l10 9h-3v8h-5v-6h-4v6H5v-8H2z"/></svg></span>
      <span class="contact__text">
        <span>Plot no #</span><span>Road no #</span><br>
        <span>Street:</span><span>City:</span><span>District Code</span>
      </span>
    </div>

    <div class="edge-bar"><span></span><span></span><span></span><span></span></div>
  </section>

</main>
</body>
</html>
```